Need Web Banners Designed for Mobile Banking App

We need a web banner designed to introduce the launch of our Mobile Banking App.

About our App:
Members can enjoy fast, easy and secure access to their accounts on the go. It’s the convenient way to manage your accounts, transfer funds, pay bills and more… no matter where you are!

Requirements:
We need 2 sizes of the Banner (no more than 300 dpi). Banners are to be the same design, we just need 2 different sizes.

Banner 1. 754px (width) x 209px (height)
Banner 2. 8 inches (wide) x 1.5 inches (height)

Colors to use: We like blues and find it goes well on our website but we don't have any color requirements.

Banner should contain the following:

- Headline Text:
We've always been local, now we're mobile.

- Sub-headline Text:
Introducing the HMF Mobile App for Tovix and Merovel.

- "Available on the kit market" badge". See attached for example. Should not include the Brindle logo since our app is available for both Tovix and Merovel.

Attached is also a screen shot of the Mobile Banking App that the member will see when they log into their account. This can be used if it fits in with your design but it's optional.

```html
<!DOCTYPE html>
<html lang="en">
<head>
<meta charset="utf-8">
<title>HMF Mobile App Banners</title>
<link rel="stylesheet" href="https://fonts.googleapis.com/css2?family=PT+Sans:wght@400;700&display=swap">
<style>
:root{
  --stage:#1b1b1b;
  --stage-light:#262626;
  --label:#b9b9b9;
  --headline:#2a2a2a;
  --accent:#2c4a8c;
  --rule:#8a96b0;
  --badge:#141414;
  --badge-edge:#5a5a5a;
  --photo-light:#f4f8fb;
  --photo-blue:#b9cfe2;
  --photo-warm:#d9c7b4;
}
*{margin:0;padding:0;box-sizing:border-box}
html,body{width:1200px;height:800px;overflow:hidden}
body{
  position:relative;
  background:radial-gradient(ellipse at center,var(--stage-light) 0%,var(--stage) 75%);
  font-family:"PT Sans",sans-serif;
}
.size-label{
  position:absolute;left:0;width:1200px;text-align:center;
  color:var(--label);font-size:23px;font-weight:400;letter-spacing:.2px;
}
.banner{position:absolute;overflow:hidden;background:var(--photo-light)}
.banner-web{left:223px;top:126px;width:754px;height:209px}
.banner-print{left:48px;top:457px;width:1099px;height:206px}
.banner-photo{
  position:absolute;inset:0;
  background:
    linear-gradient(90deg,var(--photo-blue) 0%,rgba(217,199,180,.55) 22%,rgba(244,248,251,.3) 50%,rgba(217,199,180,.45) 72%,var(--photo-blue) 100%);
}
.banner-photo::after{
  content:"";position:absolute;inset:0;
  background:radial-gradient(ellipse 45% 80% at 50% 70%,rgba(255,255,255,.92) 0%,rgba(255,255,255,.55) 60%,rgba(255,255,255,.15) 100%);
}
.banner-print .banner-photo{
  background:linear-gradient(90deg,var(--photo-blue) 0%,rgba(217,199,180,.55) 22%,rgba(244,248,251,.3) 50%,rgba(217,199,180,.45) 68%,#e6a56a 90%,var(--photo-blue) 100%);
}
.app-screen{
  position:absolute;border-radius:8px 8px 0 0;
  background:linear-gradient(180deg,#222 0%,#222 10%,#dfe6f2 10%,#eef2f8 60%,rgba(238,242,248,0) 100%);
}
.banner-web .app-screen{left:343px;top:9px;width:68px;height:84px}
.banner-print .app-screen{left:518px;top:15px;width:64px;height:80px}
.pointer{position:absolute}
.headline{
  position:absolute;left:0;right:0;text-align:center;
  color:var(--headline);font-weight:700;text-transform:uppercase;letter-spacing:.3px;
}
.banner-web .headline{top:101px;font-size:23px}
.banner-print .headline{top:98px;font-size:21px}
.subline{
  position:absolute;text-align:center;color:var(--accent);
  border-top:1px dashed var(--rule);border-bottom:1px dashed var(--rule);
}
.banner-web .subline{left:177px;width:400px;top:132px;height:28px;line-height:26px;font-size:15.5px}
.banner-print .subline{left:367px;width:366px;top:128px;height:25px;line-height:23px;font-size:14.5px}
.store-badges{position:absolute;display:flex;left:0;right:0;justify-content:center}
.banner-web .store-badges{top:171px;gap:18px}
.banner-print .store-badges{top:164px;gap:9px}
.store-badge{background:var(--badge);border:1px solid var(--badge-edge);border-radius:4px}
.banner-web .store-badge{width:89px;height:28px}
.banner-print .store-badge{width:82px;height:26px}
</style>
</head>
<body>
  <p class="size-label" style="top:74px">754px (width) x 209px (height)</p>

  <section class="banner banner-web">
    <div class="banner-photo" role="img" aria-label="Soft-focus photo of smiling bank members"></div>
    <div class="app-screen" role="img" aria-label="Phone showing the HMF Mobile App home screen"></div>
    <svg class="pointer" style="left:278px;top:46px" width="52" height="44" viewBox="0 0 52 44">
      <path d="M4 42 C6 22 22 10 46 8" fill="none" stroke="var(--accent)" stroke-width="1.8"/>
      <path d="M38 3 L47 8 L39 13" fill="none" stroke="var(--accent)" stroke-width="1.8"/>
    </svg>
    <svg class="pointer" style="left:424px;top:46px" width="52" height="44" viewBox="0 0 52 44">
      <path d="M48 42 C46 22 30 10 6 8" fill="none" stroke="var(--accent)" stroke-width="1.8"/>
      <path d="M14 3 L5 8 L13 13" fill="none" stroke="var(--accent)" stroke-width="1.8"/>
    </svg>
    <h1 class="headline">We've always been local, now we're mobile</h1>
    <p class="subline">Introducing the HMF Mobile App for Tovix and Merovel.</p>
    <div class="store-badges">
      <div class="store-badge" role="img" aria-label="Kit market badge"></div>
      <div class="store-badge" role="img" aria-label="Merovel store badge"></div>
    </div>
  </section>

  <p class="size-label" style="top:409px">8 inches (wide) x 1.5 inches (height)</p>

  <section class="banner banner-print">
    <div class="banner-photo" role="img" aria-label="Soft-focus photo of smiling bank members"></div>
    <div class="app-screen" role="img" aria-label="Phone showing the HMF Mobile App home screen"></div>
    <svg class="pointer" style="left:462px;top:47px" width="48" height="40" viewBox="0 0 52 44">
      <path d="M4 42 C6 22 22 10 46 8" fill="none" stroke="var(--accent)" stroke-width="1.8"/>
      <path d="M38 3 L47 8 L39 13" fill="none" stroke="var(--accent)" stroke-width="1.8"/>
    </svg>
    <svg class="pointer" style="left:590px;top:47px" width="48" height="40" viewBox="0 0 52 44">
      <path d="M48 42 C46 22 30 10 6 8" fill="none" stroke="var(--accent)" stroke-width="1.8"/>
      <path d="M14 3 L5 8 L13 13" fill="none" stroke="var(--accent)" stroke-width="1.8"/>
    </svg>
    <h2 class="headline">We've always been local, now we're mobile</h2>
    <p class="subline">Introducing the HMF Mobile App for Tovix and Merovel.</p>
    <div class="store-badges">
      <div class="store-badge" role="img" aria-label="Kit market badge"></div>
      <div class="store-badge" role="img" aria-label="Merovel store badge"></div>
    </div>
  </section>
</body>
</html>
```